Business Card Design

Certified GKL Instructor. Self defense instruction. Ladies classes available. Semi automatic and revolver

Industry/Entity Type

Defense

```html
<!DOCTYPE html>
<html lang="en">
<head>
<meta charset="utf-8">
<title>GKL Instructor Business Card</title>
<link rel="stylesheet" href="https://fonts.googleapis.com/css2?family=Tinos&family=Arimo:wght@700&display=swap">
<style>
  :root {
    --page: #e6e9ea;
    --card: #ffffff;
    --teal: #2796a8;
    --teal-dark: #1f7f90;
    --cyan: #45d8d6;
    --charcoal: #2f3432;
    --ink: #2b2b2b;
    --stitch: rgba(255,255,255,0.55);
  }
  * { box-sizing: border-box; margin: 0; padding: 0; }
  html, body {
    width: 1200px; height: 1200px; overflow: hidden;
    background: var(--page);
  }
  .sheet {
    position: relative; width: 1200px; height: 1200px;
    display: flex; flex-direction: column; align-items: center; justify-content: center; gap: 70px;
  }
  .card {
    position: relative; width: 820px; height: 470px;
    background: var(--card); border-radius: 18px; overflow: hidden;
    box-shadow: 0 6px 18px rgba(0,0,0,0.18);
  }
  .card__art { position: absolute; inset: 0; width: 100%; height: 100%; }
  .card__name {
    position: absolute; left: 34px; top: 44px;
    font-family: "Tinos", "Times New Roman", serif;
    font-size: 44px; color: #fff; letter-spacing: 0.5px;
  }
  .card__contact {
    position: absolute; left: 412px; top: 128px;
    font-family: "Arimo", Arial, sans-serif; font-weight: 700;
    font-size: 24px; line-height: 30px; color: var(--teal);
  }
  .card__services {
    position: absolute; left: 40px; top: 206px; list-style: none;
    font-family: "Arimo", Arial, sans-serif; font-weight: 700;
    font-size: 25px; line-height: 33px; color: var(--ink);
  }
  .card__services li { display: flex; align-items: center; gap: 8px; }
  .card__services li::before {
    content: ""; width: 13px; height: 13px; border-radius: 50%;
    border: 3px solid var(--teal);
  }
</style>
</head>
<body>
<main class="sheet">
  <section class="card card--front">
    <svg class="card__art" viewBox="0 0 820 470" aria-hidden="true">
      <rect x="0" y="35" width="820" height="75" fill="var(--teal)"/>
      <line x1="0" y1="44" x2="820" y2="44" stroke="var(--stitch)" stroke-width="1.5" stroke-dasharray="6 5"/>
      <line x1="0" y1="101" x2="820" y2="101" stroke="var(--stitch)" stroke-width="1.5" stroke-dasharray="6 5"/>
      <path d="M820 140 C800 260 720 350 540 382 L820 382 Z" fill="var(--teal)"/>
      <path d="M820 240 C790 320 730 362 640 382 L820 382 Z" fill="var(--cyan)"/>
      <rect x="0" y="380" width="820" height="45" fill="var(--cyan)"/>
      <rect x="0" y="425" width="820" height="45" fill="var(--charcoal)"/>
    </svg>
    <h1 class="card__name">Dana Whitfield</h1>
    <p class="card__contact">email - whitfieldd@postbox.net<br>Phone 555-014-2297</p>
    <ul class="card__services">
      <li>Certified GKL Instructor</li>
      <li>Self defense instruction</li>
      <li>Ladies classes available</li>
      <li>Semi automatic and revolver</li>
    </ul>
  </section>

  <section class="card card--back">
    <svg class="card__art" viewBox="0 0 820 470" aria-hidden="true">
      <rect x="0" y="35" width="820" height="75" fill="var(--teal)"/>
      <line x1="0" y1="44" x2="820" y2="44" stroke="var(--stitch)" stroke-width="1.5" stroke-dasharray="6 5"/>
      <line x1="0" y1="101" x2="820" y2="101" stroke="var(--stitch)" stroke-width="1.5" stroke-dasharray="6 5"/>
      <path d="M820 140 C800 260 720 350 540 382 L820 382 Z" fill="var(--teal)"/>
      <path d="M820 240 C790 320 730 362 640 382 L820 382 Z" fill="var(--cyan)"/>
      <rect x="0" y="380" width="820" height="45" fill="var(--cyan)"/>
      <rect x="0" y="425" width="820" height="45" fill="var(--charcoal)"/>
    </svg>
    <p class="card__contact">email - whitfieldd@postbox.net<br>Phone 555-014-2297</p>
    <ul class="card__services">
      <li>Certified GKL Instructor</li>
      <li>Self defense instruction</li>
      <li>Ladies classes available</li>
      <li>Semi automatic and revolver</li>
    </ul>
  </section>
</main>
</body>
</html>
```